Business Card Design

We are looking for a business card designed for our landscaping company. We do landscaping installation & Maintenance Services. We would like to see designs that have basic landscaping in background. We also think it is important to have both of our names and phone numbers on the card. We need something that stands out a little whether it is shape of the card or thickness or design.

Industry/Entity Type

Business

Contact Information for Business Card

Prairie Oak Yardworks, prairieoakyard@mailbox-demo.net, Dale Pruitt 555-613-2907, Marcus Delgado 555-287-4163

```html
<!DOCTYPE html>
<html lang="en">
<head>
<meta charset="utf-8">
<title>Prairie Oak Yardworks – Business Card</title>
<link rel="stylesheet" href="https://fonts.googleapis.com/css2?family=Poiret+One&family=Roboto+Condensed:wght@400&display=swap">
<style>
  :root {
    --page-bg: #e9e7e3;
    --charcoal: #2a2a2b;
    --teal: #0fa292;
    --white: #ffffff;
    --garden-light: #7fb34a;
    --garden-dark: #2f5a22;
    --silver-light: #f4f4f4;
    --silver-dark: #8d9093;
  }
  html, body {
    margin: 0;
    width: 1200px;
    height: 1000px;
    overflow: hidden;
    background: var(--page-bg);
  }
  .canvas {
    width: 1200px;
    height: 1000px;
    display: flex;
    align-items: center;
    justify-content: center;
  }
  .business-card {
    width: 1050px;
    height: 600px;
    box-shadow: 0 14px 36px rgba(0,0,0,0.22);
  }
  .business-card svg { display: block; }
  .company-name {
    font-family: "Poiret One", sans-serif;
    font-size: 66px;
    fill: var(--white);
  }
  .contact-line {
    font-family: "Roboto Condensed", sans-serif;
    font-size: 25px;
    fill: var(--white);
  }
  .contact-icon { fill: var(--white); }
</style>
</head>
<body>
<main class="canvas">
  <div class="business-card">
    <svg width="1050" height="600" viewBox="0 0 1050 600" xmlns="http://www.w3.org/2000/svg">
      <defs>
        <linearGradient id="garden-tones" x1="0" y1="0" x2="0.6" y2="1">
          <stop offset="0" stop-color="var(--garden-dark)"/>
          <stop offset="0.5" stop-color="var(--garden-light)"/>
          <stop offset="1" stop-color="var(--garden-dark)"/>
        </linearGradient>
        <linearGradient id="silver-edge" x1="0" y1="0" x2="1" y2="1">
          <stop offset="0" stop-color="var(--silver-dark)"/>
          <stop offset="0.45" stop-color="var(--silver-light)"/>
          <stop offset="0.7" stop-color="var(--silver-dark)"/>
          <stop offset="1" stop-color="var(--silver-light)"/>
        </linearGradient>
      </defs>

      <rect class="contact-panel" x="0" y="0" width="1050" height="600" fill="var(--teal)"/>
      <rect class="title-band" x="0" y="0" width="1050" height="240" fill="var(--charcoal)"/>

      <path class="garden-photo" role="img" aria-label="Photo of a landscaped garden with rounded boxwood shrubs, ornamental grasses and trees"
            d="M0 0 H400 L600 350 Q620 390 590 430 L480 600 H0 Z" fill="url(#garden-tones)"/>

      <path class="silver-edge" d="M410 0 L612 350 Q632 390 602 432 L492 600"
            fill="none" stroke="url(#silver-edge)" stroke-width="16"/>

      <text class="company-name" x="530" y="110">Prairie Oak</text>
      <text class="company-name" x="620" y="185">Yardworks</text>

      <text class="contact-line" x="955" y="305" text-anchor="end">prairieoakyard@mailbox-demo.net</text>
      <g class="contact-icon email-icon" transform="translate(975 283)">
        <rect x="0" y="0" width="38" height="26" rx="2"/>
        <path d="M2 3 L19 15 L36 3" fill="none" stroke="var(--teal)" stroke-width="2.5"/>
      </g>

      <text class="contact-line" x="955" y="395" text-anchor="end">Dale Pruitt 555-613-2907,</text>
      <text class="contact-line" x="955" y="427" text-anchor="end">Marcus Delgado</text>
      <g class="contact-icon home-icon" transform="translate(975 370)">
        <path d="M19 0 L40 19 H34 V36 H24 V25 H14 V36 H4 V19 H-2 Z"/>
      </g>

      <text class="contact-line" x="955" y="515" text-anchor="end">555-287-4163</text>
      <g class="contact-icon phone-icon" transform="translate(978 492)">
        <path d="M7 0 L13 8 L9 13 Q14 21 21 25 L26 21 L34 27 L30 34 Q20 36 10 26 Q0 16 2 5 Z"/>
      </g>
    </svg>
  </div>
</main>
</body>
</html>
```